Meridian Callware business card design

I would like to see some designs for a business card for Meridian Callware. I would like the business card to be double sided. It will need to have a similar colour / look and feel to our website www.meridiancallware.com.au I have also attached our latest flyer. Final designs to be handed over in Photoshop format so that I can edit the business card when needed please.

Industry/Entity Type

Business

Contact Information for Business Card

Kelvin Ashworth
sales@meridiancallware.com.au
Business Development Manager
ph: (08) 6517 2984
www.meridiancallware.com.au

Font styles to use
Serif
Sans Serif

Requirements
Must have
• If you could please utilise our colour scheme as seen on our website and the attached flyer.
• I would also like the final design to be in a Photoshop format so that I can edit it when needed please.

```html
<!DOCTYPE html>
<html lang="en">
<head>
<meta charset="utf-8">
<title>Meridian Callware – Business Card</title>
<link href="https://fonts.googleapis.com/css2?family=Open+Sans:wght@400;600&display=swap" rel="stylesheet">
<style>
  :root {
    --backdrop: #e9e7e4;
    --card: #ffffff;
    --brand-blue: #1b7dc1;
    --ink: #1f1f1f;
    --ink-soft: #333333;
  }
  * { margin: 0; padding: 0; box-sizing: border-box; }
  html, body {
    width: 1200px;
    height: 1000px;
    overflow: hidden;
    background: var(--backdrop);
    font-family: "Open Sans", Arial, sans-serif;
  }
  .canvas { position: relative; width: 1200px; height: 1000px; }
  .card {
    position: absolute;
    left: 265px;
    width: 665px;
    height: 397px;
    background: var(--card);
    border-radius: 22px;
    box-shadow: 0 4px 14px rgba(0,0,0,0.18);
    overflow: hidden;
  }
  .card--front { top: 73px; }
  .card--back { top: 532px; }

  .wordmark {
    color: var(--brand-blue);
    font-weight: 600;
    letter-spacing: -0.5px;
    white-space: nowrap;
  }
  .card--front .wordmark {
    position: absolute;
    left: 32px;
    top: 72px;
    font-size: 38px;
  }
  .holder { position: absolute; left: 33px; top: 200px; }
  .holder__name {
    color: var(--brand-blue);
    font-size: 21px;
    font-weight: 600;
    line-height: 28px;
  }
  .holder__role {
    color: var(--ink);
    font-size: 16px;
    line-height: 22px;
  }
  .contacts {
    position: absolute;
    left: 33px;
    top: 286px;
    list-style: none;
  }
  .contacts li {
    display: flex;
    align-items: center;
    height: 25px;
    font-size: 16px;
    color: var(--ink);
  }
  .contacts svg {
    width: 15px;
    height: 15px;
    margin-right: 8px;
    fill: var(--brand-blue);
  }

  .card--back .brand-lockup {
    position: absolute;
    left: 0; right: 0;
    top: 150px;
    text-align: center;
  }
  .card--back .wordmark { font-size: 48px; line-height: 60px; }
  .tagline {
    font-size: 23px;
    color: var(--ink-soft);
    margin-top: 2px;
  }
</style>
</head>
<body>
<main class="canvas">
  <section class="card card--front" aria-label="Business card front">
    <div class="wordmark">Meridian Callware</div>
    <div class="holder">
      <div class="holder__name">Kelvin Ashworth</div>
      <div class="holder__role">Business Development Manager</div>
    </div>
    <ul class="contacts">
      <li>
        <svg viewBox="0 0 16 16" aria-hidden="true"><path d="M2 6c0-2 2-3 6-3s6 1 6 3v1h-3V5.5c-1-.4-5-.4-6 0V7H2zM4 8h8l2 5H2z"/></svg>
        (08) 6517 2984
      </li>
      <li>
        <svg viewBox="0 0 16 16" aria-hidden="true"><path d="M1 4h14v1L8 10 1 5zM1 6.5l7 5 7-5V12H1z"/></svg>
        sales@meridiancallware.com.au
      </li>
      <li>
        <svg viewBox="0 0 16 16" aria-hidden="true"><path d="M8 1a7 7 0 1 0 0 14A7 7 0 0 0 8 1zm0 2c1 0 2 .5 2.5 1.5-1 .3-1 1-2 1s-1.5 1-1 2 2 0 2.5 1-1 2-1.5 3.5A5 5 0 0 1 4 5c1 0 1.5 1 2.5.5S7 3 8 3z"/></svg>
        www.meridiancallware.com.au
      </li>
    </ul>
  </section>

  <section class="card card--back" aria-label="Business card back">
    <div class="brand-lockup">
      <div class="wordmark">Meridian Callware</div>
      <div class="tagline">Phone systems for your business</div>
    </div>
  </section>
</main>
</body>
</html>
```